Website for "Grupo de Tecnicas Renovadas"

We need a new web design for an enterprise dedicated to environment and energy saving engineering, based in Monterrey, Mexico.
They offer consulting services, mainly to enhance building designs, and they are also resellers for several products in the energy saving field.

The final design should be oriented to engineers and architects, and should communicate professionalism, innovation, environment care.

Here is the website of a partner enterprise, which does pretty much the same:

http://www.vientoclaro.example/

Target Market(s)

mainly architects and engineers looking for solutions on energy efficiency building

Industry/Entity Type

Environment

Requirements
Must have
• Entry page must be quite graphical and intuitive, must have a "products listing" and a "projects portfolio".

```html
<!DOCTYPE html>
<html lang="en">
<head>
<meta charset="utf-8">
<title>Grupo de Tecnicas Renovadas</title>
<link rel="stylesheet" href="https://fonts.googleapis.com/css2?family=Oswald:wght@400&family=Pathway+Gothic+One&display=swap">
<style>
  :root {
    --backdrop: #eef0f2;
    --page: #ffffff;
    --teal: #00a9b0;
    --orange: #f26522;
    --green: #a4c93c;
    --purple: #93278f;
    --red: #e8202a;
    --ink: #1f1f1f;
    --grey: #555a60;
    --footer: #3a3a3a;
    --divider: #8a8a8a;
  }
  * { margin: 0; padding: 0; box-sizing: border-box; }
  html, body { width: 1200px; height: 680px; overflow: hidden; background: var(--backdrop); }
  .page {
    position: absolute; left: 55px; top: 0; width: 1092px; height: 680px;
    background: var(--page);
    box-shadow: 0 0 8px rgba(0,0,0,.18);
  }
  .brand {
    position: absolute; left: 98px; top: 38px; height: 58px;
    display: flex; align-items: center; gap: 12px;
  }
  .brand-mark { width: 52px; height: 52px; border-radius: 50%; background: var(--teal); flex: none; }
  .brand-name {
    font-family: "Oswald", sans-serif; font-size: 24px; line-height: 1;
    color: var(--grey); white-space: nowrap;
  }

  .main-nav { position: absolute; left: 710px; top: 96px; display: flex; }
  .main-nav a {
    display: block; height: 24px; line-height: 25px; text-align: center;
    font-family: "Pathway Gothic One", sans-serif; font-size: 16px; color: #fff; text-decoration: none;
  }
  .nav-home { width: 70px; background: var(--teal); }
  .nav-about { width: 72px; background: var(--orange); }
  .nav-services { width: 73px; background: var(--green); }
  .nav-experience { width: 72px; background: var(--purple); }

  .nav-band { position: absolute; left: 0; top: 121px; width: 1092px; height: 24px; background: var(--teal); }

  .hero { position: absolute; left: 0; top: 145px; width: 1092px; height: 283px; overflow: hidden; }
  .hero-photo {
    position: absolute; inset: 0;
    background: linear-gradient(180deg, #3f8fd6 0%, #9fd0f2 28%, #4f6f55 48%, #2f4a34 58%, #b9c2c8 66%, #e6e9ec 80%, #c9ced2 100%);
  }
  .hero-caption {
    position: absolute; left: 0; top: 177px; width: 462px; height: 68px;
    background: rgba(255,255,255,.28);
    display: flex; align-items: center; padding-left: 98px; white-space: nowrap;
    font-family: "Pathway Gothic One", sans-serif; color: #fff;
  }
  .caption-title { font-size: 31px; line-height: 1; }
  .caption-rule { width: 2px; height: 32px; background: #fff; margin: 0 6px 0 7px; }
  .caption-sub { font-size: 21px; line-height: 1; padding-top: 5px; }
  .hero-arrow {
    position: absolute; left: 927px; width: 30px; height: 30px;
    background: rgba(255,255,255,.3);
  }
  .hero-arrow svg { display: block; }
  .arrow-next { top: 112px; }
  .arrow-prev { top: 165px; }

  .circle {
    position: absolute; width: 114px; height: 114px; border-radius: 50%;
    display: flex; align-items: center; justify-content: center;
    font-family: "Pathway Gothic One", sans-serif; font-size: 32px; color: #fff; text-decoration: none;
  }
  .circle-news { left: 94px; top: 488px; background: var(--red); }
  .circle-products { left: 609px; top: 487px; background: var(--orange); }
  .circle-portfolio { left: 746px; top: 487px; background: var(--green); }
  .circle-contact { left: 883px; top: 487px; background: var(--teal); }

  .news-divider { position: absolute; left: 231px; top: 472px; width: 2px; height: 145px; background: var(--divider); }
  .news-list {
    position: absolute; left: 254px; top: 472px; width: 290px; list-style: none;
    font-family: "Pathway Gothic One", sans-serif; font-size: 15px; line-height: 19px; color: var(--ink);
  }
  .news-item + .news-item { margin-top: 15px; }
  .news-date { display: block; }

  .site-footer { position: absolute; left: 0; top: 648px; width: 1092px; height: 32px; background: var(--footer); }
  .footer-links { position: absolute; left: 897px; top: 7px; display: flex; gap: 12px; align-items: center; }
  .social-dot { width: 18px; height: 18px; border-radius: 50%; background: #ffffff; }
</style>
</head>
<body>
<div class="page">
  <header>
    <div class="brand">
      <span class="brand-mark"></span>
      <span class="brand-name">Grupo de Tecnicas Renovadas</span>
    </div>
    <nav class="main-nav">
      <a class="nav-home" href="#">HOME</a>
      <a class="nav-about" href="#">ABOUT US</a>
      <a class="nav-services" href="#">SERVICES</a>
      <a class="nav-experience" href="#">EXPERIENCE</a>
    </nav>
    <div class="nav-band"></div>
  </header>

  <section class="hero">
    <div class="hero-photo" role="img" aria-label="Rooftop rows of solar panels under a bright sun with mountains and blue sky"></div>
    <div class="hero-caption">
      <span class="caption-title">DESIGN</span>
      <span class="caption-rule"></span>
      <span class="caption-sub">TRADITIONAL PLANTS AND RENEWABLE SOURCES</span>
    </div>
    <a class="hero-arrow arrow-next" href="#" aria-label="Next slide">
      <svg width="30" height="30" viewBox="0 0 30 30"><polyline points="9,5 21,15 9,25" fill="none" stroke="#fff" stroke-width="3"/></svg>
    </a>
    <a class="hero-arrow arrow-prev" href="#" aria-label="Previous slide">
      <svg width="30" height="30" viewBox="0 0 30 30"><polyline points="21,5 9,15 21,25" fill="none" stroke="#fff" stroke-width="3"/></svg>
    </a>
  </section>

  <main>
    <a class="circle circle-news" href="#">NEWS</a>
    <div class="news-divider"></div>
    <ul class="news-list">
      <li class="news-item">Interventions related to distributed generation plants to ensure the security of the national electricity system<span class="news-date">06/13/2013</span></li>
      <li class="news-item">Suspension of incentives for failure to comply with the requirements of Appendix A.70 of the Network Code pursuant to resolution 84/2012/R/eel<span class="news-date">06/10/2013</span></li>
    </ul>
    <a class="circle circle-products" href="#">PRODUCTS</a>
    <a class="circle circle-portfolio" href="#">PORTFOLIO</a>
    <a class="circle circle-contact" href="#">CONTACT</a>
  </main>

  <footer class="site-footer">
    <div class="footer-links">
      <svg width="26" height="17" viewBox="0 0 26 17" aria-label="Email">
        <rect x="1" y="1" width="24" height="15" fill="none" stroke="#fff" stroke-width="1.5"/>
        <polyline points="1,1 13,10 25,1" fill="none" stroke="#fff" stroke-width="1.5"/>
        <polyline points="1,16 10,8" fill="none" stroke="#fff" stroke-width="1.5"/>
        <polyline points="25,16 16,8" fill="none" stroke="#fff" stroke-width="1.5"/>
      </svg>
      <span class="social-dot" aria-label="Social network"></span>
      <span class="social-dot" aria-label="Social network"></span>
    </div>
  </footer>
</div>
</body>
</html>
```